The Quick Guard Privacy Handbook

A book cover. The book will be marketed as a promotional item for financial advisors, financial planners, independent insurance agents, bankers, and any professional who views their role as guardian of their clients assets and helping them manage risk.

```html
<!DOCTYPE html>
<html lang="en">
<head>
<meta charset="utf-8">
<title>The Quick Guard Privacy Handbook – Cover</title>
<link rel="stylesheet" href="https://fonts.googleapis.com/css2?family=Bebas+Neue&family=Baskervville:ital@0;1&display=swap">
<style>
  :root {
    --cover-navy: #3c5271;
    --title-white: #ffffff;
    --accent-gold: #f4c842;
    --quote-gold: #e9c24c;
    --display-font: "Bebas Neue", "Oswald", sans-serif;
    --body-font: "Baskervville", "Times New Roman", serif;
  }
  html, body {
    margin: 0;
    padding: 0;
    width: 1200px;
    height: 900px;
    overflow: hidden;
    background: var(--cover-navy);
  }
  .book-cover {
    position: relative;
    width: 1200px;
    height: 900px;
    background: var(--cover-navy);
    overflow: hidden;
  }
  .cover-type {
    position: absolute;
    inset: 0;
    width: 1200px;
    height: 900px;
  }
  .cover-type text {
    font-family: var(--display-font);
  }
  .title-white { fill: var(--title-white); }
  .title-gold { fill: var(--accent-gold); }

  .back-quote {
    position: absolute;
    left: 50px;
    width: 500px;
    margin: 0;
    font-family: var(--body-font);
    font-size: 15.6px;
    line-height: 18.8px;
    color: var(--title-white);
    text-align: center;
  }
  .quote-source {
    position: absolute;
    left: 50px;
    width: 500px;
    margin: 0;
    font-family: var(--body-font);
    font-size: 15.6px;
    line-height: 18.8px;
    color: var(--quote-gold);
    text-align: center;
  }
  .publisher {
    position: absolute;
    left: 57px;
    top: 811px;
    display: flex;
    align-items: center;
    gap: 6px;
  }
  .publisher-dot {
    width: 32px;
    height: 32px;
    border-radius: 50%;
    background: var(--accent-gold);
  }
  .publisher-text { display: flex; flex-direction: column; }
  .publisher-name {
    font-family: var(--display-font);
    font-size: 21px;
    line-height: 20px;
    letter-spacing: 0.5px;
    color: var(--title-white);
  }
  .publisher-tagline {
    font-family: var(--body-font);
    font-style: italic;
    font-size: 8px;
    line-height: 9px;
    color: var(--title-white);
  }
</style>
</head>
<body>
<main class="book-cover">
  <svg class="cover-type" viewBox="0 0 1200 900" xmlns="http://www.w3.org/2000/svg">
    <!-- back cover title -->
    <g class="back-title">
      <text class="title-white" x="220" y="67" font-size="10">THE</text>
      <text class="title-white" x="220" y="103" font-size="49" textLength="160" lengthAdjust="spacingAndGlyphs">QUICK GUARD</text>
      <text class="title-white" x="220" y="152" font-size="56" textLength="160" lengthAdjust="spacingAndGlyphs">PRIVACY</text>
      <text class="title-white" x="220" y="182" font-size="27" textLength="160" lengthAdjust="spacing">HANDBOOK</text>
    </g>
    <text class="title-gold back-heading" x="300" y="251" font-size="37" text-anchor="middle" textLength="327" lengthAdjust="spacingAndGlyphs">WHAT THE DATA TELLS US</text>

    <!-- front cover title -->
    <g class="front-title">
      <text class="title-white" x="651" y="111" font-size="28">THE</text>
      <text class="title-white" x="651" y="222" font-size="149" textLength="496" lengthAdjust="spacingAndGlyphs">QUICK GUARD</text>
      <text class="title-white" x="651" y="374" font-size="174" textLength="496" lengthAdjust="spacingAndGlyphs">PRIVACY</text>
      <text class="title-white" x="651" y="465" font-size="76" textLength="496" lengthAdjust="spacing">HANDBOOK</text>
    </g>
    <g class="front-subtitle">
      <text class="title-gold" x="651" y="552" font-size="72" textLength="496" lengthAdjust="spacingAndGlyphs">PROTECT YOURSELF</text>
      <text class="title-gold" x="651" y="625" font-size="76" textLength="496" lengthAdjust="spacingAndGlyphs">AND YOUR FAMILY</text>
      <text class="title-gold" x="651" y="716" font-size="100" textLength="496" lengthAdjust="spacingAndGlyphs">IN THE AI AGE</text>
    </g>
    <g class="front-tagline">
      <text class="title-white" x="651" y="765" font-size="34" textLength="496" lengthAdjust="spacingAndGlyphs">IT'S BETTER TO HAVE IT AND NOT NEED IT</text>
      <text class="title-white" x="651" y="806" font-size="40" textLength="496" lengthAdjust="spacingAndGlyphs">THAN TO NEED IT AND NOT HAVE IT</text>
    </g>
  </svg>

  <p class="back-quote" style="top:272px">" Identity theft doesn't announce itself. By the time most victims realize something is wrong, the damage is done - credit destroyed, accounts drained, a home title transferred to a stranger. Last Year, Americans 60 and older alone lost nearly $4.8 billion to online crime, across more than 147,000 complaints to the National Cyber Bureau. The same AI being used against you can be your strongest defense. But only if you know how to use it.</p>
  <p class="quote-source" style="top:404px">- National Cyber Bureau Internet Crime Report Released in 2025</p>

  <p class="back-quote" style="top:444px">" Northwind Labs' new AI found thousands of critical vulnerabilities hiding in the software on your devices - some for decades. Linkwell's Chief Security Officer said it plainly: "We're going to need people to deal with the bug-pocalypse "Cybersecurity job postings jumped 11% in Q! - and executive search firms are already turning away clients they cant staff".</p>
  <p class="quote-source" style="top:557px">- Jobscope Q1 2025. The Daily Ledger</p>

  <p class="back-quote" style="top:601px">" Today a criminal halfway around the world - armed with AI - can impersonate your voice, forge your signature, and transfer your home title without leaving their chair. The National Cyber Bureau counted over one million cybercrime complaints last year. This isn't a story about hackers in hoodies. It's a story about your family and your front door. And it starts with sixty-minutes"</p>
  <p class="quote-source" style="top:732px">- National Cyber Bureau Internet Crime Report Released in 2025</p>

  <div class="publisher">
    <span class="publisher-dot"></span>
    <div class="publisher-text">
      <span class="publisher-name">BRIGHT HARBOR PRESS</span>
      <span class="publisher-tagline">Publishers of Self Help and How to Books</span>
    </div>
  </div>
</main>
</body>
</html>
```